Web application design for investigative software

ThreadKove is an investigation web application that would organize, create visualizations and allow collaboration. It’s available to anyone and can be used by students, historians, watchdog groups, civic hackers, investigative reporters, mystery enthusiasts, authors, even conspiracy theorists.

We are looking for two related pages. The first, a splash, or front, page and the second a ‘template’ for the web application. They should both be styled the same. The only restriction is that the logo is set.

The design should also be modern and visually well organized — employing a combination of visual devices and info graphics. Keep it light and not too heavy but strong/ professional. Do not be influenced by the current colors of threadkove.example, though the colors should be compatible with the logo..

The pages should be compatible with bootstrap, mostly for it’s JS and component functionality. It can be advised by the designer that a subset of bootstrap be used.

The splash page.
Something along the lines of (though not a copy of) :
https://www.brimloft.example/advertise
http://www.palvornhosting.example/
http://www.murkelsoft.example/
http://www.vontasky.example/

I have a very rough wire frame ish html file uploaded. Use a a guide, but alternate ideas are encouraged.

The application page should have some sort of bar for at the top for system level links a header and a footer. A vertical column to the left between the header and footer for ads, though this will be dynamic as a user can pay out of seeing adds. All dynamic actions will be made by the developers at ThreadKove.

WARNING. Please do not submit pre-made templates from some template website. We can do that ourselves for free.

This project will deliver CODE. HTML, CSS and supporting graphics and files.

```html
<!DOCTYPE html>
<html lang="en">
<head>
<meta charset="utf-8">
<title>ThreadKove – Login</title>
<link href="https://fonts.googleapis.com/css2?family=Quicksand:wght@400;500&family=Open+Sans:wght@400;600&display=swap" rel="stylesheet">
<style>
  :root {
    --brand-red: #d0201c;
    --brand-red-dark: #b5140f;
    --tab-red: #dc5a45;
    --accent-salmon: #e0857b;
    --heading-red: #c9463b;
    --text-dark: #333333;
    --text-muted: #8f8f8f;
    --footer-bg: #e5e5e5;
    --panel-border: #dddddd;
    --field-border: #f26a55;
    --icon-square: #c9685a;
    --page-bg: #ffffff;
  }
  * { box-sizing: border-box; margin: 0; padding: 0; }
  html, body { width: 1200px; height: 835px; overflow: hidden; background: var(--page-bg); }
  body { position: relative; font-family: "Open Sans", Verdana, sans-serif; color: var(--text-dark); }
  a { color: inherit; text-decoration: none; }

  /* Header */
  .site-header { position: absolute; left: 156px; top: 0; width: 888px; height: 112px; }
  .header-shape { position: absolute; inset: 0; }
  .brand { position: absolute; left: 18px; top: 18px; display: flex; align-items: center; gap: 10px; }
  .brand-mark { width: 46px; height: 46px; border-radius: 50%; background: var(--brand-red); }
  .brand-name { font-family: "Open Sans", sans-serif; font-weight: 600; font-size: 27px; color: var(--brand-red); }
  .main-nav { position: absolute; left: 280px; top: 0; display: flex; height: 52px; }
  .main-nav a { font-family: "Open Sans", Arial, sans-serif; font-size: 15px; color: var(--text-dark); padding: 13px 10px 0; }
  .main-nav a.is-active { background: var(--tab-red); color: #fff; width: 54px; padding-left: 7px;
    clip-path: polygon(0 0, 100% 0, 100% 88%, 50% 100%, 0 88%); margin-right: 8px; }
  .account-links { position: absolute; right: 10px; top: 0; display: flex; font-size: 14px; }
  .account-links a { padding: 2px 8px 3px; color: #fff; }
  .account-links .login { background: var(--brand-red-dark); }
  .account-links .register { background: var(--accent-salmon); }
  .social-row { display: flex; gap: 7px; }
  .social-row span { width: 21px; height: 21px; background: var(--icon-square); display: block; }
  .site-header .social-row { position: absolute; right: 8px; top: 43px; }

  /* Ad column */
  .ad-column { position: absolute; left: 161px; top: 136px; width: 171px; height: 464px;
    background: linear-gradient(160deg, #6c3a3c 0%, #3f3a3d 35%, #2e3338 60%, #4b5560 100%); }
  .ad-vertical { position: absolute; left: 12px; top: 20px; display: flex; flex-direction: column; gap: 6px;
    font-family: "Quicksand", sans-serif; font-size: 21px; color: rgba(255,255,255,.35); line-height: 1; }
  .ad-label { position: absolute; left: 0; right: 0; top: 178px; text-align: center;
    font-family: "Quicksand", sans-serif; font-size: 38px; line-height: 54px; color: #fff; }

  /* Main panel */
  .app-panel { position: absolute; left: 354px; top: 136px; width: 685px; height: 464px; border: 1px solid var(--panel-border); }
  .panel-title { position: absolute; left: 0; right: 0; top: 18px; text-align: center;
    font-family: "Quicksand", sans-serif; font-weight: 400; font-size: 31px; line-height: 35px; color: var(--brand-red); }
  .login-card { position: absolute; left: 158px; top: 113px; width: 360px; height: 283px; border-radius: 3px;
    background: linear-gradient(#e2e2e2, #ffffff 70%, #f8f8f8); box-shadow: 0 1px 4px rgba(0,0,0,.3); }
  .field { position: absolute; left: 82px; width: 196px; height: 37px; border: 2px solid var(--field-border);
    border-radius: 4px; background: #fff; display: flex; align-items: center;
    font-family: "Quicksand", sans-serif; font-size: 20px; color: #b0b0b0; }
  .field svg { position: absolute; left: 6px; top: 6px; }
  .field span { flex: 1; text-align: center; padding-left: 14px; }
  .field-username { top: 69px; }
  .field-password { top: 122px; }
  .login-button { position: absolute; left: 82px; top: 175px; width: 196px; height: 37px; border: 1px solid #e88a7e;
    border-radius: 4px; background: var(--brand-red); color: #fff; font-family: "Quicksand", sans-serif; font-size: 22px; }

  /* Footer */
  .site-footer { position: absolute; left: 0; top: 628px; width: 1200px; height: 207px; background: var(--footer-bg);
    border-top: 4px solid var(--accent-salmon); }
  .footer-col { position: absolute; top: 20px; }
  .footer-col h3 { font-weight: 400; font-size: 15px; color: var(--heading-red); margin-bottom: 10px; }
  .footer-col li { list-style: none; font-size: 12.5px; color: var(--text-muted); line-height: 17px; }
  .col-contact { left: 161px; }
  .col-direct { left: 464px; }
  .col-related { left: 679px; }
  .col-connect { left: 920px; }
  .contact-item { display: flex; gap: 12px; font-size: 12.5px; color: var(--text-muted); line-height: 17px; margin-bottom: 14px; }
  .contact-item svg { flex: none; }
  .col-connect .social-row { margin-top: 12px; gap: 9px; }
  .copyright { position: absolute; left: 161px; top: 174px; font-size: 12px; color: var(--heading-red); }
</style>
</head>
<body>
  <header class="site-header">
    <svg class="header-shape" width="888" height="112" viewBox="0 0 888 112" aria-hidden="true">
      <defs><filter id="hs" x="-5%" y="-10%" width="110%" height="130%"><feDropShadow dx="0" dy="2" stdDeviation="2" flood-opacity=".25"/></filter></defs>
      <path d="M5 0 H883 V88 C700 60 420 60 250 86 C160 100 80 108 5 96 Z" fill="#fff" filter="url(#hs)"/>
    </svg>
    <a class="brand" href="#"><span class="brand-mark"></span><span class="brand-name">ThreadKove</span></a>
    <nav class="main-nav">
      <a class="is-active" href="#">Home</a>
      <a href="#">About</a>
      <a href="#">Services</a>
      <a href="#">Portfolio</a>
      <a href="#">FAQ</a>
      <a href="#">Contact</a>
    </nav>
    <div class="account-links"><a class="login" href="#">Login</a><a class="register" href="#">Register</a></div>
    <div class="social-row"><span></span><span></span><span></span><span></span></div>
  </header>

  <aside class="ad-column" role="img" aria-label="Advertisement space with a photograph background">
    <div class="ad-vertical" aria-hidden="true"><span>A</span><span>d</span><span>v</span><span>e</span><span>r</span><span>t</span><span>i</span><span>s</span><span>e</span><span>m</span><span>e</span><span>n</span><span>t</span></div>
    <div class="ad-label">Add<br>space</div>
  </aside>

  <main class="app-panel">
    <h1 class="panel-title">Investigation web application<br>Login panel</h1>
    <form class="login-card">
      <label class="field field-username">
        <svg width="24" height="22" viewBox="0 0 24 22" aria-hidden="true"><path d="M2 12 L9 19 L22 3" stroke="#bdbdbd" stroke-width="4" fill="none"/></svg>
        <span>Username</span>
      </label>
      <label class="field field-password">
        <svg width="22" height="24" viewBox="0 0 22 24" aria-hidden="true"><path d="M5 11 V6 a6 6 0 0 1 12 0" stroke="#bdbdbd" stroke-width="3" fill="none"/><rect x="2" y="11" width="16" height="12" rx="1" fill="#bdbdbd"/></svg>
        <span>Password</span>
      </label>
      <button class="login-button" type="button">Login</button>
    </form>
  </main>

  <footer class="site-footer">
    <section class="footer-col col-contact">
      <h3>Contact Us</h3>
      <div class="contact-item">
        <svg width="14" height="14" viewBox="0 0 14 14" aria-hidden="true"><rect x="1" y="4" width="12" height="9" fill="none" stroke="#8f8f8f" stroke-width="1.5"/><path d="M1 4 L7 9 L13 4 M3 4 L7 1 L11 4" fill="none" stroke="#8f8f8f" stroke-width="1.5"/></svg>
        <span>info@threadkove.example</span>
      </div>
      <div class="contact-item">
        <svg width="14" height="20" viewBox="0 0 14 20" aria-hidden="true"><rect x="2" y="1" width="10" height="18" rx="2" fill="none" stroke="#8f8f8f" stroke-width="1.6"/><circle cx="7" cy="16" r="1" fill="#8f8f8f"/></svg>
        <span>+91 900-555-0142</span>
      </div>
      <div class="contact-item">
        <svg width="14" height="20" viewBox="0 0 14 20" aria-hidden="true"><path d="M7 19 C3 12 1 9 1 7 a6 6 0 0 1 12 0 C13 9 11 12 7 19 Z" fill="#8f8f8f"/><circle cx="7" cy="7" r="2.2" fill="#e5e5e5"/></svg>
        <span>ThreadKove, Company Address<br>Ravelpur City, Nowhereland</span>
      </div>
    </section>
    <section class="footer-col col-direct">
      <h3>Direct Links</h3>
      <ul><li>Home</li><li>About</li><li>Services</li><li>Portfolio</li><li>Contact</li></ul>
    </section>
    <section class="footer-col col-related">
      <h3>Related Links</h3>
      <ul><li>Live Chat</li><li>Recent News</li><li>FAQ</li></ul>
    </section>
    <section class="footer-col col-connect">
      <h3>Connect with us</h3>
      <div class="social-row"><span></span><span></span><span></span><span></span></div>
    </section>
    <p class="copyright">© 2014 &nbsp;threadkove.example</p>
  </footer>
</body>
</html>
```